Tooth Fairy Certificates with a Brown Tooth Fairy character on it (animation)
Tooth Certificate
I needs a name and date slot
also boxes for checks or stars next to each word
- clean
- shiny
- needs more brushing

Great Job, I'm so Proud of you! keep up the great brushing!

I need 4 per 11x8 page or 2- 5' 7 per page.

```html
<!DOCTYPE html>
<html lang="en">
<head>
<meta charset="utf-8">
<title>Tooth Fairy Certificate</title>
<link rel="stylesheet" href="https://fonts.googleapis.com/css2?family=Josefin+Sans:wght@400&family=Fredoka:wght@700&family=Dancing+Script:wght@700&family=Gochi+Hand&family=Gaegu:wght@400&display=swap">
<style>
  :root {
    --night: #262459;
    --paper: #ffffff;
    --sun: #f7c21a;
    --sun-edge: #e0a40c;
    --ink-navy: #25265a;
    --ink-green: #3c6b4d;
    --rule-teal: #2e8a8c;
    --box-line: #3a5a48;
    --wing-mint: #a9e3e2;
    --gown-pink: #f4b7cf;
    --tooth-cream: #fbf1d4;
    --tooth-blue: #b9dcf3;
  }
  * { margin: 0; padding: 0; box-sizing: border-box; }
  html, body { width: 857px; height: 1200px; overflow: hidden; background: var(--night); }

  .certificate {
    position: relative;
    width: 900px;
    height: 1260px;
    transform: scale(0.95222);
    transform-origin: top left;
    overflow: hidden;
  }
  .night-pattern {
    position: absolute; inset: 0;
    background: radial-gradient(circle at 30% 20%, #2f2d6a 0%, var(--night) 60%);
  }
  .paper-blob { position: absolute; inset: 0; width: 900px; height: 1260px; }

  .art { position: absolute; }
  .art-tooth-crown { left: 132px; top: 216px; width: 110px; height: 74px; border-radius: 45%; background: linear-gradient(90deg, var(--gown-pink), #fff 50%, var(--gown-pink)); }
  .art-tooth-cool { left: 602px; top: 218px; width: 128px; height: 78px; border-radius: 45%; background: linear-gradient(90deg, var(--tooth-blue), #e6f3fb); }
  .art-tooth-fairy-peek { left: 752px; top: 455px; width: 160px; height: 320px; border-radius: 50% 0 0 50%; background: linear-gradient(90deg, var(--wing-mint), var(--tooth-cream) 45%, var(--wing-mint)); }
  .art-brown-fairy { left: 16px; top: 656px; width: 220px; height: 266px; border-radius: 40%; background: linear-gradient(160deg, #6b4532 0%, var(--gown-pink) 45%, #f9dcea 100%); }
  .art-fairy-row { left: 0; top: 1095px; width: 900px; height: 165px; background: linear-gradient(90deg, #5ba8b0 0%, #8a5a3c 25%, var(--night) 50%, #8a5a3c 75%, #5ba8b0 100%); opacity: .55; }
  .art-fairy-top { left: 0; top: 0; width: 900px; height: 140px; background: linear-gradient(90deg, var(--wing-mint), var(--sun) 20%, var(--night) 50%, var(--sun) 80%, var(--wing-mint)); opacity: .45; }

  .text { position: absolute; left: 0; width: 900px; text-align: center; }
  .title-kicker { top: 244px; left: -10px; font-family: "Josefin Sans", sans-serif; font-size: 38px; letter-spacing: 5px; color: var(--ink-navy); }
  .title-main {
    top: 286px; left: -10px;
    font-family: "Fredoka", sans-serif; font-weight: 700; font-size: 74px; letter-spacing: 1px;
    color: var(--sun); -webkit-text-stroke: 1.5px var(--sun-edge);
  }
  .awarded { top: 366px; left: -10px; font-family: "Dancing Script", cursive; font-size: 34px; color: var(--ink-navy); }
  .field-label { font-family: "Gochi Hand", cursive; font-size: 30px; color: var(--ink-green); }
  .label-name { top: 434px; left: -6px; }
  .label-date { top: 560px; left: -6px; }

  .field-rule { position: absolute; left: 160px; width: 580px; height: 2px; background: var(--rule-teal); }
  .rule-name { top: 515px; }
  .rule-date { top: 647px; }

  .checklist { position: absolute; left: 279px; top: 690px; list-style: none; }
  .checklist li { display: flex; align-items: center; height: 73px; }
  .check-box { width: 47px; height: 45px; border: 2px solid var(--box-line); margin-right: 28px; }
  .check-word { font-family: "Gaegu", cursive; font-size: 44px; color: var(--sun); }

  .praise { top: 928px; left: 20px; font-family: "Dancing Script", cursive; font-size: 36px; line-height: 70px; color: var(--ink-green); }
</style>
</head>
<body>
  <main class="certificate">
    <div class="night-pattern" role="img" aria-label="Night sky pattern with stars, coin pouches and sleeping tooth fairies"></div>
    <div class="art art-fairy-top" role="img" aria-label="Row of flying tooth fairies in yellow dresses"></div>
    <div class="art art-fairy-row" role="img" aria-label="Row of sleeping brown-haired tooth fairies with crowns"></div>

    <svg class="paper-blob" viewBox="0 0 900 1260" aria-hidden="true">
      <path fill="var(--paper)" d="M0 342 C120 205 300 136 470 136 C660 136 840 205 900 292 L900 880 C860 1010 700 1100 480 1102 C260 1102 80 1040 0 965 Z"/>
    </svg>

    <div class="art art-tooth-crown" role="img" aria-label="Little winged tooth with a crown"></div>
    <div class="art art-tooth-cool" role="img" aria-label="Winged tooth with sunglasses and a wand"></div>
    <div class="art art-tooth-fairy-peek" role="img" aria-label="Crowned tooth fairy peeking in from the right"></div>
    <div class="art art-brown-fairy" role="img" aria-label="Brown tooth fairy in a pink starry dress holding a star"></div>

    <p class="text title-kicker">TOOTH FAIRY</p>
    <h1 class="text title-main">CERTIFICATE</h1>
    <p class="text awarded">Awarded to</p>

    <p class="text field-label label-name">Name</p>
    <div class="field-rule rule-name"></div>
    <p class="text field-label label-date">Date</p>
    <div class="field-rule rule-date"></div>

    <ul class="checklist">
      <li><span class="check-box"></span><span class="check-word">Clean</span></li>
      <li><span class="check-box"></span><span class="check-word">Shiny</span></li>
      <li><span class="check-box"></span><span class="check-word">Needs more brushing</span></li>
    </ul>

    <p class="text praise">Great Job, I'm so Proud of you! keep<br>up the great brushing!</p>
  </main>
</body>
</html>
```